Online business manager needs a website

I need a website designed and then coded. I am an online business manager serving a number of different industries providing administrative support to existing small businesses and helping solo practitioners get their new business up and running.

I didn't have a logo formally designed but have been using the attached avatar and wouldn't mind something that incorporated that.

The business doesn't have an official name, so I've just been using my name Lena Pruvost, Online Business Manager or Lena Pruvost, OBM. I've attached two documents that I have made previously for an example of content.

I would prefer the final site be in Wordpress.

Requirements
Must have
• A way to contact me, testimonials, list of services

```html
<!DOCTYPE html>
<html lang="en">
<head>
<meta charset="utf-8">
<title>Lena Pruvost – Online Business Manager</title>
<link rel="stylesheet" href="https://fonts.googleapis.com/css2?family=Merriweather:ital,wght@0,300;0,400;0,700;1,400;1,700&family=Red+Hat+Display:ital,wght@0,400;0,500;0,700;0,900;1,400&display=swap">
<style>
:root{
  --purple:#7a46d8;
  --purple-deep:#6a3bd1;
  --cyan:#4dcfe9;
  --yellow:#f4e15b;
  --green:#72eea9;
  --dark:#25242b;
  --grey:#f4f4f6;
  --ink:#1f1f24;
  --white:#fff;
  --serif:'Merriweather',Georgia,serif;
  --sans:'Red Hat Display',Arial,sans-serif;
}
*{margin:0;padding:0;box-sizing:border-box}
html,body{width:1200px;height:4178px;overflow:hidden}
body{position:relative;background:var(--grey);font-family:var(--sans);color:var(--ink)}
.backdrop{position:absolute;left:0;top:0}
.abs{position:absolute}
.header{position:absolute;left:0;top:0;width:1200px;height:75px;background:var(--white);box-shadow:0 1px 6px rgba(0,0,0,.05)}
.brand{position:absolute;left:125px;top:22px;display:flex;align-items:center;gap:10px}
.brand-mark{width:32px;height:32px;background:var(--purple);border-radius:4px}
.brand-name{font:700 15px/1 var(--sans);letter-spacing:.5px}
.brand-sub{font:400 9px/1.3 var(--sans);color:#555}
.nav{position:absolute;top:30px;font:500 10px/1 var(--sans);color:var(--ink)}
.nav.active{color:var(--cyan)}
.nav-phone{color:var(--purple)}
.btn{position:absolute;display:flex;align-items:center;justify-content:center;border-radius:20px;font:700 7.5px/1 var(--sans);letter-spacing:.6px;text-transform:uppercase}
.btn-outline-cyan{border:2px solid var(--cyan);color:var(--cyan)}
.btn-outline-white{border:1.5px solid var(--white);color:var(--white)}
.btn-cyan{background:var(--cyan);color:var(--white)}
.hero-title{position:absolute;left:125px;top:142px;font:300 34px/45px var(--serif);color:var(--white)}
.hero-title em{font-style:italic;font-weight:700}
.c-cyan{color:var(--cyan)}.c-yellow{color:var(--yellow)}
.section-label{position:absolute;width:400px;left:400px;text-align:center}
.section-label .rule{position:absolute;left:199px;top:-24px;width:1.5px;height:28px;background:var(--ink)}
.section-label .kicker{font:400 11px/1 var(--serif);padding-left:40px}
.section-label .title{font:900 31px/1.2 var(--sans);margin-top:4px;text-transform:uppercase}
.on-dark .rule{background:var(--white)}
.on-dark{color:var(--white)}
.photo{position:absolute}
.service-name{position:absolute;width:250px;text-align:center;font:700 16px/19px var(--serif)}
.about-card{position:absolute;left:200px;top:1502px;width:399px;height:305px;background:var(--white);text-align:center}
.about-card .kicker{font:400 11px/1 var(--serif);margin-top:88px;padding-left:40px}
.about-card .rule{position:absolute;left:199px;top:65px;width:1.5px;height:28px;background:var(--ink)}
.about-card h2{font:900 29px/1 var(--sans);margin-top:10px}
.about-card p{font:400 19px/28px var(--serif);margin:18px 40px 0}
.about-panel{position:absolute;left:600px;top:1565px;width:399px;height:344px;background:var(--purple-deep);color:var(--white);padding:62px 50px 0 49px;font:400 10.5px/15px var(--sans)}
.about-panel p+p{margin-top:15px}
.industry{position:absolute;width:182px;height:182px;border-radius:50%;background:var(--white);box-shadow:0 6px 22px rgba(0,0,0,.05);text-align:center;font:700 13px/1 var(--serif)}
.industry svg{display:block;margin:50px auto 14px}
.arrow{position:absolute;font:400 16px/1 var(--sans)}
.quote{position:absolute;left:340px;width:520px;top:2644px;text-align:center;font:italic 400 14.5px/22px var(--sans);color:var(--white)}
.quote-mark{position:absolute;left:560px;width:80px;top:2588px;text-align:center;font:700 30px/1 var(--sans);color:var(--yellow)}
.quote-name{position:absolute;left:400px;width:400px;top:2754px;text-align:center;font:500 12px/1 var(--sans);color:var(--yellow)}
.quote-role{position:absolute;left:400px;width:400px;top:2774px;text-align:center;font:400 9px/1 var(--sans);color:var(--white)}
.tip-card{position:absolute;width:214px;height:113px;background:var(--white);padding:30px 22px 0}
.tip-card .date{font:500 8px/1 var(--sans);color:var(--purple)}
.tip-card .text{font:400 12.5px/16px var(--serif);margin-top:8px}
.tip-badge{position:absolute;left:-12px;top:-12px;width:26px;height:26px;border-radius:50%;background:var(--white);display:flex;align-items:center;justify-content:center}
.tip-card .tip-badge{left:22px;top:-13px}
.field{position:absolute;border-bottom:1px solid #55545c;font:400 10.5px/1 var(--sans);color:#d8d8dc;padding-bottom:10px}
.or{position:absolute;left:560px;width:80px;top:3885px;text-align:center;font:400 12px/1 var(--serif);color:#5c5b63}
.contact-email{position:absolute;left:400px;width:400px;top:3956px;text-align:center;font:400 13px/1 var(--sans);color:var(--white)}
.contact-phone{position:absolute;left:400px;width:400px;top:3976px;text-align:center;font:500 30px/1 var(--sans);color:var(--purple)}
.social{position:absolute;top:4036px;width:32px;height:32px;border-radius:50%;border:1.5px solid #6b6a72;display:flex;align-items:center;justify-content:center}
.social span{width:8px;height:8px;border-radius:50%;background:#d8d8dc}
.social.current{background:#d8d8dc}
.social.current span{background:var(--dark)}
.footer-note{position:absolute;left:300px;width:600px;top:4116px;text-align:center;font:400 9.5px/1 var(--sans);color:#c8c8cc}
</style>
</head>
<body>

<svg class="backdrop" width="1200" height="4178" viewBox="0 0 1200 4178" aria-hidden="true">
  <defs>
    <linearGradient id="heroGrad" x1="0" y1="0" x2="1" y2="1">
      <stop offset="0" stop-color="#7b48da"/><stop offset="1" stop-color="#6a3ed4"/>
    </linearGradient>
    <linearGradient id="testiGrad" x1="0" y1="0" x2="1" y2="0">
      <stop offset="0" stop-color="#8a5ae0"/><stop offset="1" stop-color="#6f3fd6"/>
    </linearGradient>
  </defs>
  <rect x="0" y="75" width="1200" height="1200" fill="var(--cyan)"/>
  <polygon points="0,75 1200,75 1200,389 0,603" fill="url(#heroGrad)"/>
  <polygon points="0,2514 1200,2360 1200,2790 0,2939" fill="url(#testiGrad)"/>
  <polygon points="0,3479 1200,3322 1200,4178 0,4178" fill="var(--dark)"/>
  <!-- decorations -->
  <circle cx="1108" cy="882" r="15" fill="none" stroke="var(--purple)" stroke-width="6"/>
  <polygon points="92,1035 160,1015 130,1082" fill="none" stroke="var(--yellow)" stroke-width="5"/>
  <circle cx="108" cy="1062" r="16" fill="none" stroke="var(--purple)" stroke-width="7"/>
  <path d="M1038 636 q12 12 24 6 q14 -6 26 6 l8 10" fill="none" stroke="var(--yellow)" stroke-width="5" stroke-linecap="round"/>
  <path d="M1200 835 a200 200 0 0 0 -176 180" fill="none" stroke="#fff" stroke-width="1" stroke-dasharray="4 4" opacity=".6"/>
  <polygon points="866,1876 938,1876 902,1936" fill="none" stroke="var(--yellow)" stroke-width="5"/>
  <circle cx="917" cy="1907" r="16" fill="none" stroke="var(--cyan)" stroke-width="7"/>
  <path d="M252 1938 q12 12 24 6 q14 -6 26 6 l14 24" fill="none" stroke="var(--green)" stroke-width="5" stroke-linecap="round"/>
  <circle cx="165" cy="2366" r="16" fill="none" stroke="var(--purple)" stroke-width="6"/>
  <circle cx="1075" cy="2374" r="28" fill="none" stroke="var(--green)" stroke-width="8"/>
  <path d="M0 2396 a180 180 0 0 1 310 72" fill="none" stroke="var(--green)" stroke-width="1.5" stroke-dasharray="4 5"/>
  <path d="M1200 2600 a190 190 0 0 0 -12 380" fill="none" stroke="#fff" stroke-width="1" stroke-dasharray="4 4" opacity=".5"/>
  <circle cx="1059" cy="2921" r="16" fill="none" stroke="var(--cyan)" stroke-width="6"/>
  <path d="M75 2998 q12 12 24 6 q14 -6 26 6 l20 22" fill="none" stroke="var(--green)" stroke-width="5" stroke-linecap="round"/>
  <polygon points="112,3426 208,3432 160,3500" fill="none" stroke="var(--purple)" stroke-width="5"/>
  <circle cx="178" cy="3462" r="22" fill="none" stroke="var(--green)" stroke-width="7"/>
  <path d="M1036 3488 q12 12 24 6 q14 -6 26 6 l20 20" fill="none" stroke="var(--green)" stroke-width="5" stroke-linecap="round"/>
  <circle cx="125" cy="3917" r="30" fill="none" stroke="var(--cyan)" stroke-width="8"/>
  <path d="M1200 3620 a170 170 0 0 0 -58 260" fill="none" stroke="#5a5962" stroke-width="1" stroke-dasharray="4 4"/>
  <polygon points="918,4125 1050,4052 1040,4178" fill="none" stroke="var(--purple)" stroke-width="5"/>
  <path d="M747 480 a60 60 0 0 0 140 130" fill="none" stroke="var(--dark)" stroke-width="1.5"/>
  <text x="845" y="120" fill="var(--yellow)" font-size="16">✦</text>
  <text x="710" y="252" fill="var(--yellow)" font-size="14">✦</text>
  <text x="1110" y="278" fill="var(--yellow)" font-size="14">✦</text>
</svg>

<header class="header">
  <div class="brand">
    <span class="brand-mark"></span>
    <div><div class="brand-name">LENA PRUVOST</div><div class="brand-sub">Online Business Manager</div></div>
  </div>
  <span class="nav active" style="left:472px">Home</span>
  <span class="nav" style="left:519px">About Me</span>
  <span class="nav" style="left:585px">Services</span>
  <span class="nav" style="left:645px">Testimonials</span>
  <span class="nav" style="left:725px">Blog</span>
  <span class="nav" style="left:767px">Contact Us</span>
  <span class="nav nav-phone" style="left:848px">✆ 555-014-2290</span>
  <a class="btn btn-outline-cyan" style="left:963px;top:21px;width:111px;height:31px">Work with me</a>
</header>

<h1 class="hero-title">Providing<br><em class="c-cyan">administrative support</em><br>to existing small businesses<br>and helping solo practitioners<br>get their <em class="c-yellow">new business up</em><br><em class="c-yellow">and running.</em></h1>
<a class="btn btn-cyan" style="left:125px;top:438px;width:112px;height:31px">Work with me</a>

<svg class="abs" style="left:735px;top:140px" width="440" height="440" viewBox="0 0 440 440">
  <path role="img" aria-label="Portrait photo of a smiling manager holding a tablet in a bright office" d="M120 60 q100 -60 180 20 q100 10 110 140 q10 150 -150 200 q-180 30 -230 -130 q-30 -140 90 -230z" fill="#c9c3b8"/>
  <ellipse cx="42" cy="42" rx="72" ry="62" fill="var(--cyan)"/>
  <text x="42" y="34" text-anchor="middle" font-family="Red Hat Display, sans-serif" font-size="9" font-weight="700" fill="var(--yellow)">WORK &amp; GROW</text>
  <text x="42" y="56" text-anchor="middle" font-family="Merriweather, serif" font-size="19" fill="var(--purple)">together</text>
</svg>

<div class="section-label" style="top:609px"><span class="rule"></span><div class="kicker">explore</div><div class="title">My services</div></div>
<div class="photo" role="img" aria-label="Photo of a woman on the phone with a laptop at home" style="left:200px;top:683px;width:249px;height:281px;background:linear-gradient(160deg,#e7e1da,#b8a89a)"></div>
<div class="photo" role="img" aria-label="Photo of a smiling assistant wearing a headset at a brick wall" style="left:475px;top:683px;width:250px;height:281px;background:linear-gradient(160deg,#b35a3c,#e9e4df)"></div>
<div class="photo" role="img" aria-label="Photo of colleagues discussing work at an office desk" style="left:749px;top:683px;width:250px;height:281px;background:linear-gradient(160deg,#dfe6e8,#8a8f94)"></div>
<div class="service-name" style="left:200px;top:981px">Online business<br>manager</div>
<div class="service-name" style="left:475px;top:981px">Virtual assistant</div>
<div class="service-name" style="left:749px;top:981px">Systems consultant</div>

<svg class="abs" style="left:0;top:1038px" width="1200" height="682" viewBox="0 0 1200 682">
  <polygon role="img" aria-label="Photo of a smiling woman working on a laptop in a café" points="0,154 1200,0 1200,527 0,681" fill="url(#aboutPhoto)"/>
  <defs><linearGradient id="aboutPhoto" x1="0" y1="0" x2="1" y2="0"><stop offset="0" stop-color="#6d5546"/><stop offset=".5" stop-color="#b9a898"/><stop offset="1" stop-color="#e8e4df"/></linearGradient></defs>
</svg>

<div class="about-card">
  <span class="rule"></span>
  <div class="kicker">hello i'm</div>
  <h2>LENA PRUVOST</h2>
  <p>Lorem ipsum dolor sit amet, consectetur adipiscing elit, sed do eiusmod tempor.</p>
</div>
<div class="about-panel">
  <p>There are many variations of passages of Lorem Ipsum available, but the majority have suffered alteration in some form, by injected humour, or randomised words which don't look even slightly believable. If you are going to use a passage of Lorem Ipsum, you need to be sure there isn't anything embarrassing.</p>
  <p>hidden in the middle of text. All the Lorem Ipsum generators on the Internet tend to repeat predefined chunks as necessary, making this the first true generator on the Internet ...</p>
</div>
<a class="btn btn-outline-white" style="left:649px;top:1818px;width:100px;height:29px">About me</a>

<div class="section-label" style="top:2021px"><span class="rule"></span><div class="kicker">work with</div><div class="title">Industries</div></div>
<span class="arrow" style="left:157px;top:2178px">‹</span>
<span class="arrow" style="left:1033px;top:2178px">›</span>
<div class="industry" style="left:199px;top:2097px">
  <svg width="56" height="50" viewBox="0 0 56 50" fill="none" stroke="var(--purple)" stroke-width="2"><rect x="4" y="30" width="8" height="18"/><rect x="16" y="24" width="8" height="24"/><rect x="28" y="28" width="8" height="20"/><rect x="40" y="16" width="8" height="32"/><path d="M4 26 L18 14 L30 22 L48 6" stroke="var(--cyan)"/><circle cx="48" cy="6" r="5"/></svg>Finance</div>
<div class="industry" style="left:405px;top:2097px">
  <svg width="56" height="50" viewBox="0 0 56 50" fill="none" stroke="var(--purple)" stroke-width="2"><path d="M22 10h12v8h8v12h-8v8H22v-8h-8V18h8z" stroke="var(--cyan)"/><path d="M4 40 q14 -6 24 2 q12 6 24 -4"/><path d="M4 12 q14 -6 24 2"/></svg>Health care</div>
<div class="industry" style="left:611px;top:2097px">
  <svg width="56" height="50" viewBox="0 0 56 50" fill="none" stroke="var(--purple)" stroke-width="2"><path d="M14 48V14l16-10v44M30 20l12 6v22"/><path d="M8 48h40"/><path d="M20 18v6M20 30v6M24 16v6" stroke="var(--cyan)"/></svg>Real estate</div>
<div class="industry" style="left:817px;top:2097px">
  <svg width="56" height="50" viewBox="0 0 56 50" fill="none" stroke="var(--purple)" stroke-width="2"><path d="M6 38 q22 -8 44 0 M6 44 q22 -8 44 0"/><circle cx="28" cy="18" r="10" stroke="var(--cyan)"/><path d="M14 22 q14 -12 30 -8"/></svg>Education</div>
<a class="btn btn-outline-cyan" style="left:543px;top:2311px;width:112px;height:29px">Work with me</a>

<div class="photo" role="img" aria-label="Soft photo of a desk with a laptop and coffee behind the testimonials" style="left:0;top:2520px;width:1200px;height:10px;opacity:0"></div>
<div class="section-label on-dark" style="top:2518px"><span class="rule"></span><div class="kicker">i love my clients</div><div class="title">Happy customer</div></div>
<div class="quote-mark">66</div>
<p class="quote">“Sed ut perspiciatis unde omnis iste natus error sit voluptatem accusantium doloremque laudantium, totam rem aperiam, eaque ipsa quae ab illo inventore veritatis et quasi architecto beatae vitae dicta.”</p>
<div class="quote-name">STANDARD CHUNK</div>
<div class="quote-role">Lorem ipsum</div>
<svg class="abs" style="left:986px;top:2595px" width="16" height="92" viewBox="0 0 16 92" fill="none" stroke="#fff" stroke-width="1"><circle cx="8" cy="8" r="5"/><circle cx="8" cy="8" r="2" fill="#fff"/><circle cx="8" cy="24" r="5"/><circle cx="8" cy="40" r="5"/><circle cx="8" cy="56" r="5"/><circle cx="8" cy="72" r="5"/></svg>

<div class="section-label" style="top:2943px"><span class="rule"></span><div class="kicker">Read latest</div><div class="title">Business tips</div></div>
<div class="photo" role="img" aria-label="Photo of coffee and a phone beside a laptop" style="left:200px;top:3020px;width:249px;height:122px;background:linear-gradient(150deg,#4b3a30,#cfc8c1)"></div>
<div class="photo" role="img" aria-label="Photo looking up at office towers" style="left:475px;top:3020px;width:250px;height:122px;background:linear-gradient(180deg,#9ac4e4,#2f4a66)"></div>
<div class="photo" role="img" aria-label="Photo of a business team meeting around a laptop" style="left:749px;top:3020px;width:250px;height:122px;background:linear-gradient(150deg,#2c3038,#c7cdd3)"></div>
<div class="tip-card" style="left:216px;top:3142px"><span class="tip-badge">▦</span><div class="date">11 DEC 2021</div><div class="text">Lorem Ipsum is simply dummy text of the printing and typese ...</div></div>
<div class="tip-card" style="left:491px;top:3142px"><span class="tip-badge">▦</span><div class="date">11 DEC 2021</div><div class="text">Lorem Ipsum is simply dummy text of the printing and typese ...</div></div>
<div class="tip-card" style="left:766px;top:3142px"><span class="tip-badge">▦</span><div class="date">11 DEC 2021</div><div class="text">Lorem Ipsum is simply dummy text of the printing and typese ...</div></div>
<a class="btn btn-outline-cyan" style="left:551px;top:3288px;width:98px;height:29px">View all</a>

<div class="section-label on-dark" style="top:3493px"><span class="rule"></span><div class="kicker">get in touch</div><div class="title">Contact me</div></div>
<div class="field" style="left:294px;top:3578px;width:298px;padding-left:11px">Name</div>
<div class="field" style="left:608px;top:3578px;width:296px;padding-left:11px">Phone</div>
<div class="field" style="left:294px;top:3622px;width:610px;padding-left:11px">Email</div>
<div class="field" style="left:294px;top:3666px;width:610px;height:102px;padding-left:11px">How cane i help you?</div>
<a class="btn btn-outline-white" style="left:551px;top:3796px;width:98px;height:29px">Send</a>
<div class="or">OR</div>
<div class="contact-email">hello@pruvostdesk.com</div>
<div class="contact-phone">555-014-2290</div>
<span class="social" style="left:527px"><span></span></span>
<span class="social current" style="left:565px"><span></span></span>
<span class="social" style="left:602px"><span></span></span>
<span class="social" style="left:639px"><span></span></span>
<div class="footer-note">© 2023 Lena Pruvost, OBM. All Right Reserved &nbsp;&nbsp;·&nbsp;&nbsp; Policies &amp; Terms</div>

</body>
</html>
```